Flyer Template

I need a flyer template for door knocking on properties. Text Boxes need to be editable, with a header and text body. Footer to be my info. Project to be stylized to match my real estate signs and logo art from past projects

```html
<!DOCTYPE html>
<html lang="en">
<head>
<meta charset="utf-8">
<title>Brandvik Realty – Door Knocking Flyer</title>
<link rel="stylesheet" href="https://fonts.googleapis.com/css2?family=Roboto+Condensed:wght@700&family=Open+Sans:wght@400&family=Roboto:wght@700&display=swap">
<style>
  :root {
    --red: #e3161d;
    --red-dark: #b80f14;
    --black: #0d0d0d;
    --white: #ffffff;
    --paper: #f4f4f4;
    --card: #ececec;
    --ink: #111111;
    --divider: #6a6a6a;
  }
  * { margin: 0; padding: 0; box-sizing: border-box; }
  html, body { width: 900px; height: 1200px; overflow: hidden; background: var(--white); }
  .flyer { position: relative; width: 900px; height: 1200px; background: var(--paper); overflow: hidden; font-family: "Open Sans", Arial, sans-serif; }

  .brand { position: absolute; left: 40px; top: 170px; width: 250px; text-align: center; }
  .brand-mark { width: 56px; height: 56px; border-radius: 50%; background: var(--red); margin: 0 auto 24px; }
  .brand-name { font-family: "Roboto", Arial, sans-serif; font-weight: 700; font-size: 42px; line-height: 1.4; color: var(--ink); letter-spacing: 0.5px; }

  .hero-photo { position: absolute; left: 296px; top: 0; width: 604px; height: 362px;
    background: radial-gradient(ellipse at 45% 70%, #c9733a 0%, #7a3a1c 45%, #3a1c10 100%); }

  .about-band { position: absolute; left: 0; top: 403px; width: 900px; height: 347px; background: linear-gradient(180deg, #1c1c1c 0%, #0a0a0a 60%, #2a2a2a 100%); }
  .band-rule { position: absolute; left: 0; top: 424px; width: 900px; height: 8px; background: var(--red); }
  .about-tab { position: absolute; left: 542px; top: 437px; width: 358px; height: 44px; background: var(--red);
    clip-path: polygon(14px 0, 100% 0, 100% 100%, 0 100%);
    font-family: "Roboto Condensed", Arial, sans-serif; font-weight: 700; font-size: 33px; color: var(--white);
    display: flex; align-items: center; justify-content: center; }

  .headline { position: absolute; left: 50px; top: 478px; width: 395px; text-align: center; color: var(--white);
    font-family: "Roboto Condensed", Arial, sans-serif; font-weight: 700; }
  .headline span { display: block; }
  .headline .line-1 { font-size: 62px; line-height: 66px; }
  .headline .line-2 { font-size: 86px; line-height: 80px; }
  .headline .line-3 { font-size: 20.5px; line-height: 28px; }
  .headline .line-4 { font-size: 50px; line-height: 52px; }

  .band-divider { position: absolute; left: 467px; top: 470px; width: 1px; height: 225px; background: var(--divider); }
  .about-text { position: absolute; left: 494px; top: 502px; width: 380px; color: var(--white);
    font-size: 14px; line-height: 17.6px; text-align: justify; }

  .services-tab { position: absolute; left: 0; top: 739px; width: 342px; height: 47px; background: var(--red);
    clip-path: polygon(0 0, 96% 0, 100% 100%, 0 100%);
    font-family: "Roboto Condensed", Arial, sans-serif; font-weight: 700; font-size: 33px; color: var(--white);
    display: flex; align-items: center; justify-content: center; padding-right: 10px; }
  .services-rule { position: absolute; left: 330px; top: 762px; width: 570px; height: 12px; background: #cfcfcf; }
  .services-rule-red { position: absolute; left: 0; top: 774px; width: 900px; height: 10px; background: var(--red); }

  .services { position: absolute; left: 0; top: 784px; width: 900px; height: 338px;
    background: linear-gradient(180deg, #bdbdbd 0%, #d8d8d8 45%, #e6e6e6 100%); }
  .service-card { position: absolute; top: 10px; width: 270px; height: 305px; background: var(--card); }
  .service-card:nth-child(1) { left: 35px; }
  .service-card:nth-child(2) { left: 320px; }
  .service-card:nth-child(3) { left: 605px; }
  .service-icon { width: 86px; height: 86px; border-radius: 50%; background: var(--white); border: 2px solid var(--ink); margin: 14px auto 0; }
  .service-text { margin: 26px auto 0; width: 236px; font-size: 14px; line-height: 17px; color: var(--ink); text-align: justify; text-align-last: left; }

  .footer { position: absolute; left: 0; top: 1122px; width: 900px; height: 78px; display: flex;
    font-family: "Roboto Condensed", Arial, sans-serif; font-weight: 700; font-size: 29px; color: var(--white); }
  .footer-call { width: 437px; background: var(--red); display: flex; align-items: center; justify-content: flex-end; padding-right: 14px; }
  .footer-web { flex: 1; background: var(--red-dark); display: flex; align-items: center; padding-left: 22px; }
</style>
</head>
<body>
<main class="flyer">
  <div class="hero-photo" role="img" aria-label="Photo of a log and stone lodge-style house lit warmly at dusk"></div>

  <header class="brand">
    <div class="brand-mark"></div>
    <div class="brand-name">BRANDVIK<br>REALTY</div>
  </header>

  <section class="about">
    <div class="about-band"></div>
    <div class="band-rule"></div>
    <h2 class="about-tab">ABOUT US</h2>
    <h1 class="headline">
      <span class="line-1">WE BELIEVE</span>
      <span class="line-2">CREATING</span>
      <span class="line-3">A BETTER WORLD STARTS WITH HELPING</span>
      <span class="line-4">OUR NEIGHBORS</span>
    </h1>
    <div class="band-divider"></div>
    <p class="about-text">Lorem Ipsum is simply dummy text of the printing and typesetting industry. Lorem Ipsum has been the industry's standard dummy text ever since the 1500s, when an unknown printer took a galley of type and scrambled it to make a type specimen book. It has survived not only five centuries, but also the leap into electronic typesetting, remaining essentially unchanged. It was popularised in the 1960s with the release of Tessaro sheets containing Lorem Ipsum passages, and more recently with desktop publishing software like Quillon PageSmith including versions of Lorem Ipsum.</p>
  </section>

  <div class="services-rule"></div>
  <div class="services-rule-red"></div>
  <h2 class="services-tab">SERVICES</h2>

  <section class="services">
    <article class="service-card">
      <div class="service-icon"></div>
      <p class="service-text">Lorem Ipsum is simply dummy text of the printing and typesetting industry. Lorem Ipsum has been the industry's standard dummy text ever since the 1500s, when an unknown printer took a galley of type and scrambled it to make a type specimen book. It has survived not only five centuries, but</p>
    </article>
    <article class="service-card">
      <div class="service-icon"></div>
      <p class="service-text">Lorem Ipsum is simply dummy text of the printing and typesetting industry. Lorem Ipsum has been the industry's standard dummy text ever since the 1500s, when an unknown printer took a galley of type and scrambled it to make a type specimen book. It has survived not only five centuries, but</p>
    </article>
    <article class="service-card">
      <div class="service-icon"></div>
      <p class="service-text">Lorem Ipsum is simply dummy text of the printing and typesetting industry. Lorem Ipsum has been the industry's standard dummy text ever since the 1500s, when an unknown printer took a galley of type and scrambled it to make a type specimen book. It has survived not only five centuries, but</p>
    </article>
  </section>

  <footer class="footer">
    <div class="footer-call">CALL US-123 1234 123</div>
    <div class="footer-web">WWW.MYWEBSITE.COM</div>
  </footer>
</main>
</body>
</html>
```